Driving-coach/trainer who wants to inform about the offer and how I can help people to drive more re

I need a flyer that informs potential customers about my offer.

DL size 210 mm x 99 mm, vertical!

I'm a trainer/coach who helps people to drive a car more relaxed, without fear and more confident.

It's a one to one training. I do train people in their own car. It gets people their freedom back to go where and when they like to go by own car...

Target Market(s)

People (man an woman) who are afraid of driving a car, or are very stressed while driving....

Industry/Entity Type

Life Coaching

Font styles to use
Sans Serif

Colors
acd136

Requirements
Must have
• Page 1:
• -my offer (see text-pdf)
• -three fotos (see attached files "Pixmarra") of people who are satisfied with my offer
• Page 2:
• -advantages in the work with me.
• -contact information
• -and a picture of me (see attached file) next to the contact information or the advantages of my work
• -my logo (see attached file) on Page 1 + 2
• -i like a "clear" and structured layout. "Less is more"

```html
<!DOCTYPE html>
<html lang="de">
<head>
<meta charset="utf-8">
<title>Fahrangst Flyer</title>
<link href="https://fonts.googleapis.com/css2?family=Roboto:wght@300;400;700&family=Roboto+Condensed:wght@400;700&family=Quicksand:wght@500&display=swap" rel="stylesheet">
<style>
:root{
  --green:#3f9a3e;
  --green-dark:#2f7f31;
  --green-deep:#276e29;
  --grey-band:#cfd1d3;
  --ink:#1f1f1f;
  --white:#ffffff;
  --page:#e9e8e4;
}
*{margin:0;padding:0;box-sizing:border-box}
html,body{width:1200px;height:1200px;overflow:hidden;background:var(--page)}
body{position:relative;font-family:"Roboto Condensed",sans-serif;color:var(--ink)}
.flyer{position:absolute;top:76px;width:448px;height:1048px;background:var(--white);overflow:hidden;box-shadow:0 6px 18px rgba(0,0,0,.18)}
.flyer--front{left:118px}
.flyer--back{left:634px}
.abs{position:absolute}
svg.shape{position:absolute;left:0;display:block}

/* front */
.front-title{top:36px;left:0;width:100%;text-align:center;color:var(--white);font-family:"Roboto",sans-serif;font-weight:700;font-size:37px;line-height:44px;z-index:2}
.front-questions{top:190px;left:41px;width:330px;font-size:24px;line-height:24px;z-index:2}
.front-questions p{margin-bottom:11px}
.photo{background:linear-gradient(120deg,#e6ddd0 0%,#d9b48c 35%,#9fa7ad 70%,#5f6b74 100%)}
.front-photo{top:300px;left:0;width:448px;height:270px}
.front-photo::after{content:"";position:absolute;left:0;top:0;width:100%;height:60px;background:linear-gradient(180deg,#fff,rgba(255,255,255,0))}
.cta-badge{top:424px;left:250px;width:184px;height:184px;border-radius:50%;background:radial-gradient(circle at 40% 35%,#4fae49,var(--green));color:var(--white);font-weight:700;font-size:28px;line-height:34px;text-align:center;display:flex;align-items:center;justify-content:center;z-index:2}
.situations{top:582px;left:38px;width:372px;color:var(--white);z-index:3}
.situations h2{font-family:"Roboto",sans-serif;font-weight:300;font-size:28px;line-height:33px;margin-bottom:10px}
.situations ul{list-style:none}
.situations li{position:relative;padding-left:18px;font-size:16px;line-height:21px;padding-bottom:8px;margin-bottom:8px;border-bottom:2px solid rgba(255,255,255,.4)}
.situations li:last-child{border-bottom:none}
.situations li::before{content:"";position:absolute;left:0;top:6px;width:10px;height:10px;border-radius:50%;background:var(--white)}
.foot-strip{left:0;bottom:0;width:100%;height:46px;background:var(--green-deep);z-index:1}

/* back */
.step-num-big{top:27px;left:-8px;width:90px;height:90px;border-radius:50%;background:radial-gradient(circle at 40% 35%,#4fae49,var(--green-dark));color:var(--white);font-family:"Roboto",sans-serif;font-weight:700;font-size:60px;line-height:90px;text-align:center;padding-left:14px}
.back-title{top:52px;left:94px;color:var(--white);font-family:"Roboto",sans-serif;font-weight:700;font-size:37px}
.back-photo{top:140px;left:0;width:448px;height:246px}
.step{top:290px;width:128px;height:128px;border-radius:50%;background:radial-gradient(circle at 40% 35%,#4fae49,var(--green-dark));border:4px solid #e4e4e4;color:var(--white);text-align:center;display:flex;flex-direction:column;align-items:center;justify-content:center;box-shadow:0 3px 6px rgba(0,0,0,.2)}
.step b{font-size:30px;line-height:32px}
.step span{font-weight:700;font-size:13px;line-height:17px;padding:0 10px}
.step--1{left:26px}.step--2{left:160px}.step--3{left:294px}
.benefits{top:450px;left:34px;width:388px;list-style:none}
.benefits li{position:relative;padding-left:19px;font-size:16.5px;line-height:21px;margin-bottom:11px}
.benefits li::before{content:"";position:absolute;left:0;top:6px;width:10px;height:10px;border-radius:50%;background:var(--green)}
.contact-zone{top:724px;left:0;width:448px;height:286px}
.coach-photo{top:724px;left:236px;width:212px;height:286px;background:linear-gradient(90deg,rgba(200,202,204,0) 0%,rgba(160,163,166,.8) 35%,#b9bbbd 60%,#eceded 100%)}
.contact{top:818px;left:32px;font-size:17px;line-height:21px;color:var(--ink);z-index:2}
.contact .phone{font-weight:700;font-size:24px;line-height:34px;margin-top:3px}
.name-box{top:914px;left:29px;width:312px;height:70px;background:var(--white);border-radius:10px;padding:10px 0 0 22px;font-family:"Quicksand",sans-serif;color:var(--green);box-shadow:-4px 4px 0 rgba(0,0,0,.85);z-index:2}
.name-box .name{font-size:22px;letter-spacing:2px;line-height:26px;white-space:nowrap}
.name-box .role{font-size:14px;letter-spacing:1.3px;line-height:20px;white-space:nowrap}
</style>
</head>
<body>

<section class="flyer flyer--front">
  <svg class="shape" style="top:0" width="448" height="240" viewBox="0 0 448 240">
    <path d="M0 0H448V136Q230 130 0 168Z" fill="var(--green)"/>
    <path d="M0 168Q230 130 448 136V148Q230 144 0 184Z" fill="var(--grey-band)"/>
  </svg>
  <h1 class="abs front-title">Fahrangst erfolgreich<br>loswerden!</h1>
  <div class="abs front-questions">
    <p>Sie wollen endlich entspannt und sicher Auto fahren?</p>
    <p>Panikattacken beim Autofahren überwinden?</p>
  </div>
  <div class="abs photo front-photo" role="img" aria-label="Foto: zufriedene junge Autofahrerin am offenen Autofenster zeigt Daumen hoch"></div>
  <svg class="shape" style="top:540px" width="448" height="508" viewBox="0 0 448 508">
    <path d="M0 30Q200 6 448 2V508H0Z" fill="var(--green)"/>
  </svg>
  <div class="abs cta-badge">Dann sind<br>Sie hier<br>richtig!</div>
  <div class="abs situations">
    <h2>Kommt Ihnen eine dieser Situationen bekannt vor?</h2>
    <ul>
      <li>Angst oder Panikattacken begleiten Sie beim Autofahren. Vielleicht vermeiden Sie deshalb das Autofahren komplett. - Sie möchten angstfrei und/oder ohne Panikattacken fahren.</li>
      <li>Sie trauen sich das Autofahren nicht (mehr) zu. - Sie wünschen sich, sicher, entspannt und stressfrei Auto zu fahren.</li>
      <li>Autofahren erleben Sie unter hoher Anspannung und Stress. - Sie wünschen sich, Autofahren sicher und entspannt zu erleben.</li>
      <li>Bestimmte Situationen (z.B. Autobahn, Baustellen, Stadtvekehr...) bereiten Ihnen großen Stress. - Sie möchten diese Situationen souveräner meistern.</li>
    </ul>
  </div>
  <div class="abs foot-strip"></div>
</section>

<section class="flyer flyer--back">
  <div class="abs photo back-photo" role="img" aria-label="Foto: lächelnde Frau mit Sonnenbrille im Haar am Steuer eines Cabrios"></div>
  <svg class="shape" style="top:0" width="448" height="200" viewBox="0 0 448 200">
    <path d="M0 0H448V144Q230 130 0 162Z" fill="var(--green)"/>
    <path d="M0 162Q230 130 448 144V152Q230 140 0 178Z" fill="var(--grey-band)"/>
  </svg>
  <div class="abs step-num-big">3</div>
  <h1 class="abs back-title">Schritte zur Lösung</h1>
  <div class="abs step step--1"><b>1</b><span>Erstgespräch vereinbaren</span></div>
  <div class="abs step step--2"><b>2</b><span>Analyse Ihrer individuellen Situation und Zielsetzung</span></div>
  <div class="abs step step--3"><b>3</b><span>Individuelles Coaching und Training</span></div>
  <ul class="abs benefits">
    <li>über 10 Jahre Erfahrung als Trainerin und Coach im Bereich Fahrsicherheit.</li>
    <li>Als psychotherapeutische Heilpraktikerin bin ich auf Angststörungen und Panikattacken spezialisiert.</li>
    <li>100 % auf Sie zugeschnitten: ich hole Sie genau dort ab, wo Sie jetzt stehen und unterstütze Sie in Ihrem Prozess individuell und zielführend.</li>
    <li>Wenn es Ihnen nicht möglich ist, in meine Praxis nach Brunnbach Lindenau zu kommen: Mit der mobilen Praxis komme ich auch zu Ihnen.</li>
    <li>Termine sind auch abends und am Wochenende möglich.</li>
  </ul>
  <svg class="shape contact-zone" viewBox="0 0 448 286" preserveAspectRatio="none">
    <defs><linearGradient id="contactGrey" x1="0" y1="0" x2="1" y2="0"><stop offset="0" stop-color="#e2e3e4"/><stop offset="1" stop-color="#a9acaf"/></linearGradient></defs>
    <path d="M0 96Q220 8 448 0V286H0Z" fill="url(#contactGrey)"/>
  </svg>
  <div class="abs coach-photo" role="img" aria-label="Porträtfoto der Trainerin in weißer Bluse"></div>
  <div class="abs contact">
    <p>Weitere Informationen finden Sie auf:</p>
    <p>www.fahrsicher-mit-ruhe.de</p>
    <p>Oder rufen Sie mich einfach an:</p>
    <p class="phone">Tel. 0151 23 45 67 89</p>
  </div>
  <div class="abs name-box">
    <div class="name">Sabine Hartwig</div>
    <div class="role">Fahrangst-Bewältigungs-Coach</div>
  </div>
  <div class="abs foot-strip" style="height:38px"></div>
</section>

</body>
</html>
```